Birchwell Entreprise Campus Media Package

We are looking for a designer to unify our company's image throughout its stationery and marketing deliverables. We will be focusing on:
*Business Cards (3.5 x 2)
*Letter Head (Letter Size)
*PowerPoint Presentation Template,
*One Pager Flyer (Letter Size)
*Front of Elevator's bay: 4 photos of the elevator bays (two groups of 3 elevators) to which we are looking for designs for its doors and surrounding wall (vinyl prints)
*Font's suggestions
*Official color palette.
*Outdoor Street Signage: please use the following dimensions:
Sign #1 (Richmond Side): 48(W)x72"(H) (3 sided)
Sign #2: 24"(W)x48"(H) (3 sided)
Sign #3 (Top of Hill): 30(W)x54(H) (2 sides)
*Carport Sign:
See photos attached. The white letters will be removed, and a new sign will take place. Preferably, Cut-Out fonts, but we can consider an alternative approach for cost effective solution.
Find attached the approved logos.
______________________________________
We are a real estate holding company focused on the commercial office space in the Ohio, US, market.
You can check our site at www.birchwellcampus-example.com
As inspiration guidelines, we would like to see designs that are modern, minimalistic, dynamic and energetic.
Updates
Target Market(s)
General Population, Business Owners, Non-Profit Organizations, Government
Industry/Entity Type
Real Estate - Commercial Office Space - Flex Space
Look and feel
Each slider illustrates characteristics of the customer's brand and the style your logo design should communicate.

```html
<!DOCTYPE html>
<html lang="en">
<head>
<meta charset="utf-8">
<title>Birchwell Entreprise Campus – Business Card</title>
<link href="https://fonts.googleapis.com/css2?family=Montserrat:wght@600;800&family=Roboto:wght@500&display=swap" rel="stylesheet">
<style>
  :root {
    --backdrop: #3e4552;
    --brand-blue: #1a8fd0;
    --brand-blue-light: #2a9ad6;
    --ink: #1d1e22;
    --paper: #ffffff;
  }
  * { box-sizing: border-box; margin: 0; padding: 0; }
  html, body {
    width: 1200px; height: 803px; overflow: hidden;
    background: var(--backdrop);
  }
  .canvas { position: relative; width: 1200px; height: 803px; }
  .card {
    position: absolute; top: 247px;
    width: 540px; height: 309px;
    overflow: hidden;
  }

  /* Back of card */
  .card-back { left: 40px; background: var(--brand-blue); }
  .card-back .texture {
    position: absolute; inset: 0;
    background: linear-gradient(135deg, var(--brand-blue-light), var(--brand-blue));
  }
  .company-name {
    font-family: "Montserrat", sans-serif; font-weight: 800;
    letter-spacing: 0.5px; text-transform: uppercase; white-space: nowrap;
  }
  .card-back .company-name {
    position: absolute; left: 0; right: 0; top: 138px;
    text-align: center; font-size: 24px; color: var(--paper);
  }

  /* Front of card */
  .card-front { left: 620px; background: var(--paper); }
  .card-front .band { position: absolute; left: 0; top: 0; }
  .card-front .company-name {
    position: absolute; left: 168px; top: 36px;
    font-size: 17px; color: var(--ink);
  }
  .holder {
    position: absolute; left: 168px; top: 104px;
    color: var(--ink);
  }
  .holder .full-name {
    font-family: "Montserrat", sans-serif; font-weight: 800;
    font-size: 27px; letter-spacing: 0.5px;
  }
  .holder .designation {
    font-family: "Montserrat", sans-serif; font-weight: 600;
    font-size: 10px; letter-spacing: 0.8px; margin-top: 2px;
  }
  .holder .rule { width: 72px; height: 3px; background: var(--ink); margin-top: 6px; }
  .contact {
    position: absolute; left: 168px; top: 178px;
    display: flex; gap: 14px;
  }
  .contact .icon-rail { width: 26px; height: 104px; }
  .contact ul {
    list-style: none; padding-top: 4px;
    font-family: "Roboto", sans-serif; font-weight: 500;
    font-size: 12px; color: var(--ink);
  }
  .contact li { height: 25px; line-height: 20px; white-space: nowrap; }
</style>
</head>
<body>
<main class="canvas">

  <section class="card card-back" aria-label="Business card back">
    <div class="texture" role="img" aria-label="Subtle tonal blue background texture"></div>
    <p class="company-name">Birchwell Entreprise Campus</p>
  </section>

  <section class="card card-front" aria-label="Business card front">
    <svg class="band" width="150" height="309" viewBox="0 0 150 309" aria-hidden="true">
      <polygon points="0,0 150,0 90,309 0,309" fill="var(--brand-blue)"/>
      <polygon points="30,0 130,0 72,309 10,309" fill="var(--brand-blue-light)" opacity="0.45"/>
    </svg>

    <p class="company-name">Birchwell Entreprise Campus</p>

    <div class="holder">
      <h1 class="full-name">NAME SURNAME</h1>
      <p class="designation">DESIGNATION HERE</p>
      <div class="rule"></div>
    </div>

    <div class="contact">
      <svg class="icon-rail" viewBox="0 0 26 104" aria-hidden="true">
        <rect width="26" height="104" rx="13" fill="var(--ink)"/>
        <g fill="var(--paper)" stroke="var(--paper)">
          <path d="M13 7a5 5 0 0 1 5 5c0 4-5 8-5 8s-5-4-5-8a5 5 0 0 1 5-5z" stroke="none"/>
          <circle cx="13" cy="12" r="1.8" fill="var(--ink)" stroke="none"/>
          <path d="M9 31c0 6 4 10 9 10l1-3-3-1-1 1c-2-1-3-2-4-4l1-1-1-3z" stroke="none"/>
          <rect x="7.5" y="56" width="11" height="8" fill="none" stroke-width="1.4"/>
          <path d="M7.5 56l5.5 4.5 5.5-4.5" fill="none" stroke-width="1.4"/>
          <path d="M9 79l9 5-4 1 2 4-2 1-2-4-3 3z" stroke="none"/>
        </g>
      </svg>
      <ul>
        <li>YOUR ADDRESS HERE</li>
        <li>+1 555-014-2290</li>
        <li>companyname@example.com</li>
        <li>www.birchwellcampus-example.com</li>
      </ul>
    </div>
  </section>

</main>
</body>
</html>
```